VELMO business card - High end Italian floors and coverings

We need a new design for our business card. We are an exclusive company located in Mexico.
Our commercial name is VELMO. Our legal name is Bruma Ceniza SA de CV.
We bring the latest trends in materials for floors and walls such as natural stones, wood, leather, design porcelanato tiles and so.
Our company image colors are black, white and red.
Our customers are high end architects and designers.
We are looking for an elegant but fresh design which reflects exclusivity, simplicity and reliability.
(we are working also in a new website)

Requirements
Nice to have
• back and front design
Space for 2 addresses (one for each showroom location)

```html
<!DOCTYPE html>
<html lang="es">
<head>
<meta charset="utf-8">
<title>VELMO – Tarjeta de presentación</title>
<link rel="stylesheet" href="https://fonts.googleapis.com/css2?family=Saira:wght@400;500;600&display=swap">
<style>
  :root {
    --red: #d7161e;
    --ink: #2a2a2a;
    --paper: #f6f6f4;
    --rule: #9a9a9a;
    --sketch: #d9d9d6;
    --back-dark: #1f1f1f;
    --back-mid: #4a4a4a;
    --stage: #e4e4e2;
  }
  * { box-sizing: border-box; margin: 0; padding: 0; }
  html, body { width: 1200px; height: 800px; overflow: hidden; }
  body {
    background: var(--stage);
    font-family: "Saira", sans-serif;
    display: flex;
    align-items: center;
    justify-content: center;
    gap: 40px;
  }
  .card {
    position: relative;
    width: 550px;
    height: 314px;
    box-shadow: 0 8px 24px rgba(0,0,0,.18);
  }
  .card--front { background: var(--paper); color: var(--ink); }

  .brand {
    position: absolute;
    display: flex;
    align-items: center;
    gap: 10px;
    font-weight: 500;
    font-size: 34px;
    letter-spacing: 3px;
    line-height: 1;
  }
  .brand__square { width: 14px; height: 14px; background: var(--red); }
  .card--front .brand { left: 32px; top: 42px; color: var(--red); }

  .holder { position: absolute; left: 300px; top: 40px; }
  .holder__name {
    color: var(--red);
    font-weight: 600;
    font-size: 17px;
    letter-spacing: .5px;
    text-transform: uppercase;
  }
  .holder__email {
    font-size: 10px;
    font-weight: 500;
    letter-spacing: .6px;
    text-transform: uppercase;
    margin-top: 1px;
  }

  .sketch {
    position: absolute;
    left: 36px; top: 150px;
    width: 240px; height: 140px;
    background: linear-gradient(135deg, var(--sketch), #c4c4c0);
  }

  .showroom {
    position: absolute;
    left: 300px;
    padding-left: 12px;
    border-left: 1.5px solid var(--rule);
    font-size: 10.5px;
    line-height: 1.45;
    letter-spacing: .5px;
    text-transform: uppercase;
    font-style: normal;
  }
  .showroom--gdl { top: 120px; }
  .showroom--cdmx { top: 205px; }
  .showroom__tel-label { color: var(--red); }

  .card--back {
    background: var(--back-dark);
    overflow: hidden;
  }
  .back-pattern {
    position: absolute; inset: 0;
    background:
      radial-gradient(ellipse 120% 80% at 100% 0%, #7a7a7a 0%, var(--back-mid) 35%, transparent 65%),
      linear-gradient(160deg, var(--back-mid), var(--back-dark) 70%);
  }
  .card--back .brand { right: 40px; bottom: 44px; color: #ffffff; }
</style>
</head>
<body>
  <section class="card card--front" aria-label="Frente de la tarjeta">
    <div class="brand"><span class="brand__square"></span>VELMO</div>

    <div class="holder">
      <p class="holder__name">Lucía Ferrer Ibarra</p>
      <p class="holder__email">Email: lucia@velmo.com.mx</p>
    </div>

    <div class="sketch" role="img" aria-label="Boceto a línea de fachadas y planos arquitectónicos"></div>

    <address class="showroom showroom--gdl">
      Ámbar #1870 Esq. Turín<br>
      Colonia Arcos CP 44130<br>
      Guadalajara, Jalisco<br>
      <span class="showroom__tel-label">Tel:</span> (33) 418.207.53
    </address>

    <address class="showroom showroom--cdmx">
      Lago Cristal #245<br>
      Local B 3er piso, Colonia<br>
      Marina CP 11410, Mexico, DF<br>
      <span class="showroom__tel-label">Tel:</span> (33) 240.713.98
    </address>
  </section>

  <section class="card card--back" aria-label="Reverso de la tarjeta">
    <div class="back-pattern" role="img" aria-label="Patrón de curvas amplias en grises y negro"></div>
    <div class="brand"><span class="brand__square"></span>VELMO</div>
  </section>
</body>
</html>
```